Martin Hale PA Card Logo

Current logo attached. Its 25 year old logo I have used. Looking for a new fresh elegant professional look/design for a law firm that has high net worth clientele and is estate planning business law firm. Firm mis in Palm Beach Florida.
One sided card linen stock white will be used. Logo section name section. Logo should include nice elegant design using the letter "M" perhapa (I am not wed to current font of the M on current logo.) Be creative there with logo design. My initials are MH.......color scheme I figure 3 tone... Raised Gold Foil, Blue name of firm = Martin Hale, P.A. My practice focus is Family and Business Asset Protection. My name is Martin M. Hale, Esq. Practice specialties include Asset Protection trusts, Business Succession Planning, LLC law, Estate Planning, Medicaid Planning (Maybe put those topics in bullets in a section of card. Bottom of card can be reserved smaller print address phone website and email address. Address section is not as important as logo and topics of practice on front. I foresee address section can be in dark blue. MY name and Topics dark blue as well.
Target Market(s)
affluent; business owners executives; wealth 2-10 million net worth
Industry/Entity Type
business law and estate planning
Contact Information for Business Card
White thick linen one sided

```html
<!DOCTYPE html>
<html lang="en">
<head>
<meta charset="utf-8">
<title>Martin Hale, P.A. — Business Card</title>
<link href="https://fonts.googleapis.com/css2?family=Crimson+Pro:wght@400;600;700&display=swap" rel="stylesheet">
<style>
  :root {
    --backdrop: #e9e6ea;
    --paper: #f6f5f2;
    --navy: #0f2d55;
    --gold: #c08a2b;
    --ink: #3b3b3b;
    --slate: #6d706d;
    --white: #ffffff;
  }
  * { box-sizing: border-box; margin: 0; padding: 0; }
  html, body {
    width: 1200px; height: 900px; overflow: hidden;
    background: var(--backdrop);
    font-family: "Crimson Pro", Georgia, serif;
  }
  .canvas {
    width: 1200px; height: 900px;
    display: flex; flex-direction: column; align-items: center; justify-content: center; gap: 36px;
  }
  .card {
    width: 700px; height: 400px; position: relative;
    box-shadow: 0 10px 28px rgba(0,0,0,.18);
  }
  .card--front { background: var(--paper); border-bottom: 6px solid var(--navy); }
  .card--back { background: var(--slate); }

  .logo {
    position: absolute; display: flex; align-items: center; gap: 10px;
    font-weight: 600; letter-spacing: .06em; text-transform: uppercase;
  }
  .logo__dot { width: 12px; height: 12px; border-radius: 50%; }
  .card--front .logo { top: 40px; right: 44px; color: var(--gold); font-size: 26px; }
  .card--front .logo__dot { background: var(--gold); }
  .card--back .logo { top: 50%; left: 50%; transform: translate(-50%,-50%); color: var(--white); font-size: 34px; }
  .card--back .logo__dot { background: var(--white); }

  .attorney { position: absolute; left: 44px; top: 96px; }
  .attorney__name {
    color: var(--navy); font-weight: 700; font-size: 27px;
    padding-bottom: 4px; border-bottom: 1.5px solid var(--gold); display: inline-block;
  }
  .specialties__title { color: var(--navy); font-weight: 700; font-size: 22px; margin-top: 6px; }
  .specialties__list { list-style: none; margin-top: 2px; }
  .specialties__list li {
    color: var(--ink); font-size: 17px; line-height: 1.25; padding-left: 16px; position: relative;
  }
  .specialties__list li::before {
    content: ""; position: absolute; left: 2px; top: 8px;
    width: 7px; height: 7px; border-radius: 50%; background: var(--gold);
  }

  .divider { position: absolute; left: 44px; right: 44px; top: 286px; height: 1.5px; background: var(--navy); }

  .contact { position: absolute; left: 44px; top: 300px; list-style: none; }
  .contact li { display: flex; align-items: center; gap: 8px; color: var(--ink); font-size: 15px; line-height: 1.45; }
  .contact svg { width: 13px; height: 13px; fill: var(--gold); flex: none; }

  .office { position: absolute; top: 298px; font-size: 14.5px; line-height: 1.25; color: var(--ink); }
  .office--one { left: 262px; }
  .office--two { left: 480px; }
  .office__title { display: flex; align-items: center; gap: 5px; color: var(--gold); font-weight: 700; }
  .office__title svg { width: 11px; height: 13px; fill: var(--gold); }
  .office__building { color: var(--gold); }
</style>
</head>
<body>
<main class="canvas">
  <section class="card card--front" aria-label="Card front">
    <div class="logo"><span class="logo__dot"></span>Martin Hale, P.A.</div>

    <div class="attorney">
      <h1 class="attorney__name">Martin M. Hale, Esq.</h1>
      <h2 class="specialties__title">Practice Specialties</h2>
      <ul class="specialties__list">
        <li>Asset Protection trusts</li>
        <li>Business Succession Planning, LLC law</li>
        <li>Estate Planning</li>
        <li>Medicaid Planning</li>
      </ul>
    </div>

    <div class="divider"></div>

    <ul class="contact">
      <li><svg viewBox="0 0 24 24"><path d="M6.6 10.8a15 15 0 0 0 6.6 6.6l2.2-2.2a1 1 0 0 1 1-.25 11.4 11.4 0 0 0 3.6.57 1 1 0 0 1 1 1V20a1 1 0 0 1-1 1A17 17 0 0 1 3 4a1 1 0 0 1 1-1h3.5a1 1 0 0 1 1 1c0 1.25.2 2.45.57 3.57a1 1 0 0 1-.25 1z"/></svg>555-014-2290</li>
      <li><svg viewBox="0 0 24 24"><path d="M2 5h20v14H2zm2 2v.5l8 5 8-5V7l-8 5z"/></svg>info@haleestatelaw.com</li>
      <li><svg viewBox="0 0 24 24"><path d="M12 2a10 10 0 1 0 0 20 10 10 0 0 0 0-20zm0 2c.9 0 2.2 2 2.7 5H9.3C9.8 6 11.1 4 12 4zM4.3 11h3c-.1 1.4 0 2.8.2 4H5a8 8 0 0 1-.7-4zm5 0h5.4a18 18 0 0 1-.2 4H9.5a18 18 0 0 1-.2-4zm7.4 0h3a8 8 0 0 1-.7 4h-2.5c.2-1.2.3-2.6.2-4zM12 20c-.9 0-2-1.6-2.5-3h5c-.5 1.4-1.6 3-2.5 3z"/></svg>www.haleestatelaw.com</li>
    </ul>

    <address class="office office--one">
      <div class="office__title"><svg viewBox="0 0 20 24"><path d="M10 0a8 8 0 0 0-8 8c0 6 8 16 8 16s8-10 8-16a8 8 0 0 0-8-8zm0 11a3 3 0 1 1 0-6 3 3 0 0 1 0 6z"/></svg>Coral Bend Office</div>
      <div class="office__building">Harbor Point Offices</div>
      <div>420 Palm Crest Drive</div>
      <div>Coral Bend, Florida 34990</div>
    </address>

    <address class="office office--two">
      <div class="office__title"><svg viewBox="0 0 20 24"><path d="M10 0a8 8 0 0 0-8 8c0 6 8 16 8 16s8-10 8-16a8 8 0 0 0-8-8zm0 11a3 3 0 1 1 0-6 3 3 0 0 1 0 6z"/></svg>Sandpiper Bay Office</div>
      <div class="office__building">Harbor Point Offices</div>
      <div>1580 Meridian Blvd.</div>
      <div>Sandpiper Bay, Florida 33499</div>
    </address>
  </section>

  <section class="card card--back" aria-label="Card back">
    <div class="logo"><span class="logo__dot"></span>Martin Hale, P.A.</div>
  </section>
</main>
</body>
</html>
```